Building Maintenance Flyer specialising in hot and silent pressure cleaning

Hi. I love this flyer. I would like something similar but with hot water pressure washing and building maintenance

Ferro Lane & Services provides high pressure steam cleaning and water blasting services throughout Brisbane and surrounding areas, covering the Industrial, Commercial, Strata and Residential property owners sectors.

FLS combining the cleaning power of heat with state-of-the-art silent equipment, accredited technicians and a steadfast commitment to the environment. We offer the best Prompt, Professional Service.

Fully Accredited & Certified Technicians
100% Satisfaction Guaranteed
We are a family owned and operated business and love what we do. No job is too big or too small and we take pride in our work.
All of our services are undertaken using industry leading equipment and, providing safe and superior results.

Our business is covered by 20 million full public liability insurance and we operate within strict health & safety guidelines, providing all our clients with complete peace of mind. Project plans and risk assessments can also be provided upon request.

BODY CORPORATES

BUILDING FAÇADE CLEANING

CAR PARKS – underground, single and multi level

DRIVE THRU

FOOD PRODUCTION FACILITIES CLEANING SANITISING

SHOPPING CENTRES

BIRD MANAGEMENT AND DECONTAMINATION

GENERAL MAINTENANCE

CONSTRUCTION CLEAN UPS

SPILL MANAGEMENT

CONCRETE CLEANING AND DEGRASING

CONCRETE SEALING

FACTORY CLEANING & CLEAN UP

ENVIRONMENTAL DECONTAMINATION OF HEAVY VEHICLES AND EQUIPMENT

SITE CLEANS AND RUBBISH REMOVAL

MANUFACTURING PLANTS

Target Market(s)

Facility Managers, Commercial and Industrial Property Owners, Property Managers, Schools, Restaurants,

Industry/Entity Type

Pressure Cleaning

Font styles to use
Sans Serif

Colors
0293ce
00a990
33a6d7
33b8a4

Requirements
Must have
• SILENT HOT WATER PRESSURE CLEANING
Runs up to 120 Degrees Celsius
SANITISING - Bin areas, outdoor areas, cafe's, restaurants, schools, drive thru's
Blue's and Greens to link in with our logo

```html
<!DOCTYPE html>
<html lang="en">
<head>
<meta charset="utf-8">
<title>Ferro Lane &amp; Services – Property Maintenance Flyer</title>
<link rel="stylesheet" href="https://fonts.googleapis.com/css2?family=Lato:wght@400;700;900&family=Raleway:wght@500;700;800&display=swap">
<style>
  :root {
    --page-bg: #ebebeb;
    --paper: #ffffff;
    --navy: #1f2c66;
    --navy-deep: #223070;
    --navy-light: #34458a;
    --sky: #0293ce;
    --sky-soft: #33a6d7;
    --sky-bright: #15b2e2;
    --green: #00a990;
    --green-soft: #33b8a4;
    --band: #e4f1fb;
    --ink: #23306b;
    --white: #ffffff;
    --photo-a: #6b4a36;
    --photo-b: #c9b79a;
    --photo-c: #e9d8b4;
  }
  * { margin: 0; padding: 0; box-sizing: border-box; }
  html, body { width: 1200px; height: 900px; overflow: hidden; }
  body {
    background: radial-gradient(ellipse at center, #f6f6f6 0%, var(--page-bg) 75%);
    font-family: "Lato", Arial, sans-serif;
    position: relative;
  }
  .flyer {
    position: absolute;
    left: 395px; top: 143px;
    width: 438px; height: 617px;
    background: var(--paper);
    box-shadow: 0 6px 18px rgba(0,0,0,0.18);
    overflow: hidden;
  }
  .icon-sky { fill: var(--sky-bright); }
  .icon-green { fill: var(--green-soft); }
  .line-sky { fill: none; stroke: var(--sky-bright); }
  .line-green { fill: none; stroke: var(--green-soft); }

  .brand {
    position: absolute; left: 64px; top: 34px;
    display: flex; align-items: center; gap: 10px;
  }
  .brand-dot {
    width: 22px; height: 22px; border-radius: 50%;
    background: var(--green);
  }
  .brand-name {
    font-family: "Raleway", Arial, sans-serif;
    font-weight: 800; font-size: 36px; color: var(--sky);
    letter-spacing: 1px;
  }
  .headline {
    position: absolute; left: 23px; top: 121px;
    font-family: "Raleway", Arial, sans-serif;
    line-height: 1.05;
  }
  .headline-kicker { font-size: 13px; font-weight: 500; color: var(--ink); letter-spacing: 0.2px; }
  .headline-main { font-size: 20px; font-weight: 800; color: var(--navy); }
  .headline-accent { font-size: 20px; font-weight: 800; color: var(--sky-soft); }
  .hero-photo {
    position: absolute; left: 267px; top: 0;
    width: 156px; height: 205px;
    background: linear-gradient(135deg, var(--photo-a) 0%, var(--photo-b) 55%, var(--photo-c) 100%);
  }
  .intro-band {
    position: absolute; left: 0; top: 205px; width: 100%; height: 67px;
    background: var(--band);
    display: flex; flex-direction: column; justify-content: center; align-items: center;
    font-weight: 900; font-size: 13px; color: var(--navy);
    letter-spacing: 1px; line-height: 1.6; text-align: center;
  }
  .services-panel {
    position: absolute; left: 0; top: 272px; width: 100%; height: 257px;
    background: linear-gradient(160deg, var(--navy-light) 0%, var(--navy-deep) 45%, var(--navy) 100%);
    color: var(--white);
  }
  .highlights { position: absolute; left: 37px; top: 15px; list-style: none; }
  .highlights li {
    display: flex; align-items: center; gap: 12px;
    font-weight: 900; font-size: 12.5px; letter-spacing: 0.6px;
    height: 22.5px;
  }
  .highlights svg { width: 11px; height: 11px; flex: none; }
  .divider {
    position: absolute; left: 123px; top: 95px; width: 170px; height: 2px;
    background: linear-gradient(90deg, var(--sky-bright), var(--green-soft));
  }
  .service-grid {
    position: absolute; left: 38px; top: 117px; width: 390px;
    display: grid; grid-template-columns: 224px 166px;
    row-gap: 13px; list-style: none;
  }
  .service-grid li {
    display: flex; align-items: center; gap: 9px;
    font-size: 9.5px; font-weight: 700; height: 19px;
  }
  .service-grid svg { width: 18px; height: 18px; flex: none; }
  .phone-bar {
    position: absolute; left: 0; top: 529px; width: 100%; height: 30px;
    background: var(--sky-bright);
    display: flex; justify-content: center; align-items: center; gap: 12px;
    color: var(--white); font-weight: 900; font-size: 22px; letter-spacing: 0.8px;
  }
  .phone-bar svg { width: 18px; height: 18px; }
  .contact-row {
    position: absolute; left: 32px; top: 573px; width: 374px;
    display: flex; justify-content: space-between;
    font-size: 14px; color: var(--ink);
  }
  .contact-row span { display: flex; align-items: center; gap: 9px; }
  .contact-row svg { width: 14px; height: 14px; }
  .corner-tab {
    position: absolute; right: 0; bottom: 0; width: 25px; height: 23px;
    background: var(--band);
  }
</style>
</head>
<body>
<main class="flyer">
  <div class="brand">
    <span class="brand-dot"></span>
    <span class="brand-name">FLS</span>
  </div>

  <h1 class="headline">
    <div class="headline-kicker">ALL COMMERCIAL &amp;</div>
    <div class="headline-main">INDUSTRIAL PROPERTY</div>
    <div class="headline-accent">MAINTENANCE</div>
  </h1>

  <div class="hero-photo" role="img" aria-label="Technician using a hot water pressure cleaner on paving in sunlight"></div>

  <div class="intro-band">
    <div>FLS – SERVICING BRISBANE'S</div>
    <div>COMMERCIAL &amp; INDUSTRIAL SECTOR 24/7</div>
  </div>

  <section class="services-panel">
    <ul class="highlights">
      <li><svg viewBox="0 0 12 12"><circle class="line-green" cx="6" cy="6" r="5" stroke-width="2"/></svg>WE OPERATE 24/7, 7 DAYS A WEEK</li>
      <li><svg viewBox="0 0 12 12"><circle class="icon-green" cx="6" cy="3.5" r="2.5"/><rect class="icon-green" x="2" y="7" width="8" height="5" rx="2"/></svg>SILENT HOT WATER PRESSURE CLEANING 120°C</li>
      <li><svg viewBox="0 0 12 12"><path class="icon-green" d="M6 1l5 5-5 5-5-5z"/></svg>FULLY ACCREDITED TECHNICIANS</li>
    </ul>
    <div class="divider"></div>
    <ul class="service-grid">
      <li><svg viewBox="0 0 18 18"><rect class="line-sky" x="2" y="4" width="14" height="11" stroke-width="1.5"/><path class="line-sky" d="M2 8h14" stroke-width="1.5"/></svg>Car Park Cleaning</li>
      <li><svg viewBox="0 0 18 18"><rect class="icon-green" x="4" y="2" width="10" height="14" rx="1"/></svg>Building Façade Cleaning</li>
      <li><svg viewBox="0 0 18 18"><rect class="icon-sky" x="4" y="5" width="10" height="11" rx="1"/><rect class="icon-sky" x="3" y="2" width="12" height="2"/></svg>Bin Area Sanitising</li>
      <li><svg viewBox="0 0 18 18"><circle class="line-green" cx="9" cy="9" r="7.5" stroke-width="1.5"/><path class="line-green" d="M6 12l6-6" stroke-width="1.5"/></svg>Bird Decontamination</li>
      <li><svg viewBox="0 0 18 18"><path class="icon-sky" d="M9 2l7 6h-2v8H4V8H2z"/></svg>Concrete Cleaning &amp; Sealing</li>
      <li><svg viewBox="0 0 18 18"><rect class="line-green" x="1" y="4" width="16" height="10" rx="2" stroke-width="1.5"/><circle class="icon-green" cx="5" cy="9" r="1.5"/><circle class="icon-green" cx="9" cy="9" r="1.5"/><circle class="icon-green" cx="13" cy="9" r="1.5"/></svg>Drive Thru Cleaning</li>
      <li><svg viewBox="0 0 18 18"><path class="icon-sky" d="M9 2c3 4 5 7 5 10a5 5 0 0 1-10 0c0-3 2-6 5-10z"/></svg>Spill Management</li>
      <li><svg viewBox="0 0 18 18"><rect class="icon-green" x="6" y="6" width="6" height="11" rx="1"/><rect class="icon-green" x="7" y="2" width="4" height="3"/></svg>Factory Clean Ups</li>
    </ul>
  </section>

  <div class="phone-bar">
    <svg viewBox="0 0 18 18"><path fill="#ffffff" d="M4 1l3 4-2 2c1 2 3 4 5 5l2-2 4 3-2 3C8 16 2 10 1 4z"/></svg>
    <span>1-800-5 GETFLS</span>
  </div>

  <div class="contact-row">
    <span><svg viewBox="0 0 14 14"><circle cx="7" cy="7" r="6.5" fill="#23306b"/><circle cx="7" cy="7" r="2.5" fill="#ffffff"/></svg>service@flsqld.com</span>
    <span><svg viewBox="0 0 14 14"><rect x="0.5" y="2.5" width="13" height="9" fill="none" stroke="#23306b" stroke-width="1.3"/><path d="M1 3l6 5 6-5" fill="none" stroke="#23306b" stroke-width="1.3"/></svg>www.flsqld.com</span>
  </div>
  <div class="corner-tab"></div>
</main>
</body>
</html>
```